El Molinero Brochure

Create a brochure for a new reception venue - El Molinero
www.El-Molinero.example

Here is info it must contain

Please refer to our site for inspiration - I know this is alot of info but ?

El Molinero Reception Hall
4817C Tidewell Rd, Harrow Point, CA 707-555-0148
www.El-Molinero.example

Located in Harrow Point, California, we are a new venue that can host a variety of events. We can provide an exceptional space for your next party, reception, quinceañera, birthday party, or meeting! We treat each client with respect and go out of our way to accommodate all of your needs and make your event a success. Conveniently located just off the Route 14/22 junction, El Molinero is located in a safe, well-lit area with a large private parking area.

The space comes prepared with everything you need to get your party started – chairs and tables with tablecloths, a well-equipped kitchen, and incredible decorations to set the perfect backdrop to your event! Rent just the Lounge for a more intimate get-together, or add the Main Hall for your large sit-down event.

Lounge – Beautiful 1,600 ft2 entry room featuring large living room with conversation sofa seating for 40+ Sound system  Pass-through bar with seating  Fully-equipped 200 ft2 kitchen with
4-burner gas stove, oven, large double sink, full-size refrigerator, 2 microwaves, and ice machine, plus lots of storage and counter space  Newly-remodeled Men’s and Women’s bathrooms

Main Hall – Spacious 24’x80’ room with seating for up to 160 people  2,000 ft2  72” round tables with chairs, each seating up to 8 guests  DJ stand and Sound system  Atmospheric lighting
_______________________________________
Pricing -
Daytime Parties
Available 8AM-2PM
4-hour minimum

Lounge and Kitchen Only
Fri - Sat - Sun : $80/hr
Mon - Thurs : $60/hr

All Areas: Lounge, Kitchen, Main Hall, and Backyard
Fri - Sat - Sun : $120/hr
Mon - Thurs : $100/hr
___________________________________________
Evening Events
Available 3PM-12AM
5-hour minimum

Lounge and Kitchen Only -
Fri - Sat - Sun : $100/hr
Mon - Thurs : $50/hr

Fri - Sat - Sun : $160/hr
Mon - Thurs : $75/hr
___________________________________________________
Looking for a different time frame, all-day rental, or other special request? Let us know!
We'd be happy to provide you with a custom quote for your event.

```html
<!DOCTYPE html>
<html lang="en">
<head>
<meta charset="utf-8">
<title>El Molinero Brochure</title>
<link rel="stylesheet" href="https://fonts.googleapis.com/css2?family=Open+Sans:ital,wght@0,400;0,600;0,700;1,600&family=Tinos:ital,wght@0,400;1,700&display=swap">
<style>
  :root {
    --maroon: #3b1516;
    --maroon-deep: #2e0f10;
    --cream: #e4dccb;
    --ink: #2b2222;
    --light: #f1e9df;
    --page: #eeeeee;
    --photo-warm: linear-gradient(160deg, #6b5a4a 0%, #a88e6e 45%, #3b2f28 100%);
    --photo-hall: linear-gradient(170deg, #2a221d 0%, #7a6450 40%, #c8b49a 65%, #4a3b30 100%);
    --photo-lounge: linear-gradient(165deg, #3a312c 0%, #8d8374 40%, #d9d3c7 60%, #5a4c3f 100%);
    --photo-buffet: linear-gradient(170deg, #332b26 0%, #9a8f80 45%, #c9b99f 70%, #4b3a2c 100%);
  }
  * { box-sizing: border-box; margin: 0; padding: 0; }
  html, body { width: 779px; height: 1200px; overflow: hidden; background: var(--page); }
  body { position: relative; font-family: "Open Sans", sans-serif; color: var(--ink); }

  .spread { position: absolute; left: 30px; width: 719px; height: 557px; display: flex; box-shadow: 0 6px 18px rgba(0,0,0,.18); }
  .spread--outside { top: 30px; background: var(--maroon); }
  .spread--inside { top: 613px; background: var(--maroon); padding: 9px; }

  .panel { position: relative; flex: 1 1 0; }
  .spread--outside .panel + .panel { border-left: 1px solid var(--maroon-deep); }
  .spread--inside .panel { background: var(--cream); }
  .spread--inside .panel + .panel { border-left: 1px solid #cfc5b2; }

  .photo { display: block; }

  /* outside */
  .outside-back .photo { position: absolute; left: 22px; top: 150px; width: 196px; height: 118px; background: var(--photo-warm); }
  .outside-back .note { position: absolute; left: 14px; right: 14px; top: 290px; text-align: center; color: var(--light); font-size: 11.5px; line-height: 1.45; }
  .outside-back .note p + p { margin-top: 10px; }

  .outside-info { text-align: center; color: var(--light); }
  .outside-info .name { position: absolute; left: 0; right: 0; top: 148px; font-size: 17px; font-weight: 600; letter-spacing: .3px; }
  .outside-info .contact { position: absolute; left: 0; right: 0; top: 215px; font-size: 10px; line-height: 1.55; }

  .outside-cover .photo-frame { position: absolute; left: 34px; top: 22px; width: 172px; height: 250px; border: 2px solid #8b7a66; padding: 4px; }
  .outside-cover .photo { width: 100%; height: 100%; background: var(--photo-lounge); }
  .outside-cover .name { position: absolute; right: 24px; top: 318px; color: var(--light); font-size: 20px; font-weight: 600; }

  /* inside */
  .inside-intro .photo { height: 240px; background: var(--photo-hall); }
  .inside-intro .copy { padding: 14px 14px 0; font-size: 9.2px; line-height: 1.5; }
  .inside-intro .copy p + p { margin-top: 10px; }

  .inside-spaces .photo { height: 240px; background: var(--photo-lounge); }
  .inside-spaces .copy { padding: 10px 14px 0; font-size: 9px; line-height: 1.42; }
  .inside-spaces h2 { font-size: 10px; font-weight: 600; font-style: italic; margin: 0 0 2px; }
  .inside-spaces h2 + ul { margin-bottom: 8px; }
  .inside-spaces ul { padding-left: 11px; }

  .inside-pricing .copy { padding: 12px 14px 0; font-family: "Tinos", serif; font-size: 9px; line-height: 1.22; }
  .inside-pricing h2 { font-size: 10.5px; font-weight: 700; font-style: italic; margin-bottom: 2px; }
  .inside-pricing .block { margin-bottom: 6px; }
  .inside-pricing .photo { position: absolute; left: 0; right: 0; bottom: 0; height: 200px; background: var(--photo-buffet); }
</style>
</head>
<body>

<section class="spread spread--outside" aria-label="Brochure outside">
  <div class="panel outside-back">
    <div class="photo" role="img" aria-label="Photo of two armchairs beside a lamp in the lounge"></div>
    <div class="note">
      <p>Looking for a different time frame, all-day rental, or other special request? Let us know!</p>
      <p>We'd be happy to provide you with a custom quote for your event.</p>
    </div>
  </div>
  <div class="panel outside-info">
    <div class="name">El Molinero</div>
    <div class="contact">
      El Molinero Reception Hall<br>
      4817C Tidewell Rd, Harrow Point, CA<br>
      707-555-0148<br>
      www.El-Molinero.example
    </div>
  </div>
  <div class="panel outside-cover">
    <div class="photo-frame">
      <div class="photo" role="img" aria-label="Photo of the lounge with sofas and large windows"></div>
    </div>
    <div class="name">El Molinero</div>
  </div>
</section>

<section class="spread spread--inside" aria-label="Brochure inside">
  <div class="panel inside-intro">
    <div class="photo" role="img" aria-label="Photo of the main hall with string lights and set tables"></div>
    <div class="copy">
      <p>Located in Harrow Point, California, we are a new venue that can host a variety of events. We can provide an exceptional space for your next party, reception, quinceañera, birthday party, or meeting! We treat each client with respect and go out of our way to accommodate all of your needs and make your event a success. Conveniently located just off the Route 14/22 junction, El Molinero is located in a safe, well-lit area with a large private parking area.</p>
      <p>The space comes prepared with everything you need to get your party started – chairs and tables with tablecloths, a well-equipped kitchen, and incredible decorations to set the perfect backdrop to your event! Rent just the Lounge for a more intimate get-together, or add the Main Hall for your large sit-down event.</p>
    </div>
  </div>

  <div class="panel inside-spaces">
    <div class="photo" role="img" aria-label="Photo of the lounge seating under globe lights"></div>
    <div class="copy">
      <h2>Lounge</h2>
      <ul>
        <li>Beautiful 1,600 ft2 entry room featuring large living room with conversation sofa seating for 40+ Sound system</li>
        <li>Pass-through bar with seating</li>
        <li>Fully-equipped 200 ft2 kitchen with 4-burner gas stove, oven, large double sink, full-size refrigerator, 2 microwaves, and ice machine, plus lots of storage and counter space</li>
        <li>Newly-remodeled Men's and Women's bathrooms</li>
      </ul>
      <h2>Main Hall</h2>
      <ul>
        <li>Spacious 24'x80' room with seating for up to 160 people</li>
        <li>2,000 ft2</li>
        <li>72" round tables with chairs, each seating up to 8 guests</li>
        <li>DJ stand and Sound system</li>
        <li>Atmospheric lighting</li>
      </ul>
    </div>
  </div>

  <div class="panel inside-pricing">
    <div class="copy">
      <h2>Pricing</h2>
      <div class="block">Daytime Parties<br>Available 8AM-2PM<br>4-hour minimum</div>
      <div class="block">Lounge and Kitchen Only<br>Fri - Sat - Sun : $80/hr<br>Mon - Thurs : $60/hr</div>
      <div class="block">All Areas: Lounge, Kitchen, Main Hall, and Backyard<br>Fri - Sat - Sun : $120/hr<br>Mon - Thurs : $100/hr</div>
      <div class="block">Evening Events<br>Available 3PM-12AM<br>5-hour minimum</div>
      <div class="block">Lounge and Kitchen Only -<br>Fri - Sat - Sun : $100/hr<br>Mon - Thurs : $50/hr</div>
      <div class="block">All Areas: Lounge, Kitchen, Main Hall, and Backyard<br>Fri - Sat - Sun : $160/hr<br>Mon - Thurs : $75/hr</div>
    </div>
    <div class="photo" role="img" aria-label="Photo of a buffet table set in front of tall windows"></div>
  </div>
</section>

</body>
</html>
```